Design Large Inspirational Artwork with Long Quote

Design a large piece of art with a quote from Marcus Tillwright.

QUOTE
"The thing that's so interesting about being alive is that you're all in. No matter what you do, you're all in. This is gonna kill you, so I think you might as well play the most magnificent game you can while you're waiting. Because, do you have anything better to do? Why not pick the best thing possible that you could do? Because you're more powerful than you think, way more powerful than you think. I mean, God only knows what you are in the final analysis. You're blind to your own weaknesses, but you're also blind to your own strengths. How far could you take that if you stopped wasting time, and if you stopped lying, and if you oriented yourself to the highest possible good that you could conceive of and you committed to that? How much good could you do? Well, I would say: why don't you find out?"

SIZE
A high-resolution print size of 6' wide and 3' tall should provide ample space for both the quote and the accompanying artwork.

TYPOGRAPHY
Choose a bold, clean, and easily readable font for the quote. You could also experiment with different font sizes for certain words or phrases to emphasize their importance within the quote.

COLORS
Since the quote is thought-provoking and reflective, you might want to use a color palette that evokes a sense of introspection and depth. Consider using cool, calming colors like shades of blue, gray, or green. Alternatively, you can use a contrasting color scheme with a light background and dark text to make the quote stand out.

ARTWORK
Select / create / edit background artwork to complement the quote.
While a great design might be minimalistic and/or greyscale, I'd really like to see some full color options. This might be anything from photography or graphics inspired by the ideas in the text, to abstract colors or illustrations that feel like the sentiment expressed.
The art should capture your attention and encourage you to read the text. The art should be visually appealing, both at a distance and up close, regardless of whether the text is read.
Updates

Having trouble confirming the exact print size.

Still looking for printing solution and final size confirmation.

Target Market(s)

Personal, business, office

Industry/Entity Type

None

Font styles to use
Sans Serif
Script

Requirements
Must have
• Entire quote, legible text, modern design, attractive artwork, approx 6ft wide and 3ft tall
Nice to have
• Different font (sizes) for certain words or phrases to emphasize their importance within the quote.

```html
<!DOCTYPE html>
<html lang="en">
<head>
<meta charset="utf-8">
<title>Quote Artwork</title>
<link rel="stylesheet" href="https://fonts.googleapis.com/css2?family=Roboto+Condensed:wght@400&display=swap">
<style>
  :root {
    --sky-deep: #050608;
    --sky-warm: #1a130c;
    --rain-blue: #1d4e6e;
    --rain-dark: #0c1a2a;
    --ember: #c0522a;
    --frame-grey: #8d8d8d;
    --quote-blue: #a4dcf6;
  }
  html, body {
    margin: 0;
    padding: 0;
    width: 1200px;
    height: 600px;
    overflow: hidden;
    background: var(--sky-deep);
  }
  .artwork {
    position: relative;
    width: 1200px;
    height: 600px;
    overflow: hidden;
    background:
      radial-gradient(ellipse 60% 50% at 78% 95%, var(--sky-warm) 0%, transparent 70%),
      linear-gradient(180deg, #08090b 0%, var(--sky-deep) 60%, #0d0a07 100%);
  }
  .key-photo {
    position: absolute;
    left: 0;
    top: 0;
    width: 460px;
    height: 600px;
    background:
      radial-gradient(ellipse 18% 45% at 20% 55%, rgba(255,170,80,0.55) 0%, rgba(192,82,42,0.25) 45%, transparent 75%),
      linear-gradient(90deg, var(--rain-blue) 0%, #173a58 35%, var(--rain-dark) 75%, #0f0d12 100%);
  }
  .key-photo::after {
    content: "";
    position: absolute;
    right: 0;
    top: 0;
    width: 40px;
    height: 100%;
    background: linear-gradient(90deg, transparent, var(--sky-deep));
  }
  .quote-frame {
    position: absolute;
    left: 186px;
    top: 56px;
    width: 939px;
    height: 491px;
  }
  .quote-frame svg {
    position: absolute;
    inset: 0;
    overflow: visible;
  }
  .quote-mark {
    position: absolute;
    font-family: "Roboto Condensed", sans-serif;
    font-weight: 700;
    font-size: 88px;
    line-height: 1;
    color: var(--frame-grey);
  }
  .quote-mark--open { left: 40px; top: -22px; }
  .quote-mark--close { left: 856px; top: 480px; }
  .quote-text {
    position: absolute;
    left: 22px;
    top: 17px;
    width: 894px;
    margin: 0;
    font-family: "Roboto Condensed", sans-serif;
    font-weight: 400;
    font-size: 31px;
    line-height: 38.7px;
    color: var(--quote-blue);
    text-align: justify;
    hyphens: manual;
  }
</style>
</head>
<body>
  <main class="artwork">
    <div class="key-photo" role="img" aria-label="Rain-streaked blue photograph of a glowing antique key hanging from a white rope"></div>

    <section class="quote-frame">
      <svg width="939" height="491" viewBox="0 0 939 491" aria-hidden="true">
        <g fill="none" stroke="var(--frame-grey)" stroke-width="6">
          <polyline points="40,3 3,3 3,488 40,488"/>
          <polyline points="899,3 936,3 936,488 899,488"/>
        </g>
      </svg>
      <span class="quote-mark quote-mark--open" aria-hidden="true">&ldquo;</span>
      <blockquote class="quote-text">The thing that's so interesting about being alive is that you're all in. No matter what you do, you're all in. This is gonna kill you, so I think you might as well play the most magnificent game you can while you're waiting. Because, do you have anything better to do ? Why not pick the best thing possible that you could do ? Because you're more pow&shy;erful than you think, way more powerful than you think. I mean, God only knows what you are in the final analysis. You're blind to your own weaknesses, but you're also blind to your own strengths. How far could you take that if you stopped wasting time, and if you stopped lying, and if you oriented yourself to the highest possible good that you could conceive of and you committed to that ? How much good could you do? Well, I would say: why don't you find out ?</blockquote>
      <span class="quote-mark quote-mark--close" aria-hidden="true">&rdquo;</span>
    </section>
  </main>
</body>
</html>
```